Thank You Card

I'm looking for a thank you card design using our logo and other graphics. We are an essential business and our employees (Electricians) have done an incredible job staying healthy and safe during the COVID-19 pandemic, I want to send each a thank you card.

```html
<!DOCTYPE html>
<html lang="en">
<head>
<meta charset="utf-8">
<title>Thank You Card</title>
<link href="https://fonts.googleapis.com/css2?family=Quicksand:wght@500;600;700&display=swap" rel="stylesheet">
<style>
  :root {
    --bg: #e6e6e4;
    --card: #f5f5f4;
    --red: #e8283f;
    --red-soft: #f3a3ad;
    --blue: #2b3fa6;
    --ink: #555558;
    --line: #3a3a3a;
  }
  * { box-sizing: border-box; margin: 0; padding: 0; }
  html, body { width: 1200px; height: 900px; overflow: hidden; }
  body {
    background: var(--bg);
    font-family: "Quicksand", sans-serif;
    position: relative;
  }
  .card {
    position: absolute;
    width: 540px;
    height: 360px;
    background: var(--card);
    box-shadow: 0 6px 18px rgba(0,0,0,0.14);
  }
  /* Back of postcard */
  .card-back { left: 45px; top: 270px; }
  .back-brand {
    position: absolute; left: 0; top: 0; width: 280px; height: 100%;
    display: flex; flex-direction: column; align-items: center;
  }
  .brand-name {
    margin-top: 110px;
    display: flex; align-items: center; gap: 8px;
    color: var(--red); font-weight: 700; font-size: 26px; line-height: 1.05;
    text-align: center;
  }
  .brand-mark { width: 12px; height: 12px; background: var(--red); flex: none; }
  .dot-row { margin-top: 62px; display: flex; gap: 7px; }
  .dot-row span { width: 5px; height: 5px; border-radius: 50%; background: var(--red); box-shadow: -1px 1px 0 var(--blue); }
  .contact {
    margin-top: 14px; font-size: 10px; font-weight: 500; color: var(--ink);
    text-align: center; line-height: 1.5;
  }
  .contact-line { display: flex; justify-content: center; align-items: center; gap: 4px; }
  .contact-line svg { width: 8px; height: 8px; fill: var(--red); }
  .divider { position: absolute; left: 285px; top: 50px; width: 1.5px; height: 200px; background: var(--line); }
  .stamp-box { position: absolute; right: 36px; top: 42px; width: 62px; height: 62px; border: 1.5px solid var(--line); }
  .address-line { position: absolute; left: 305px; right: 28px; top: 210px; height: 1.5px; background: var(--line); }

  /* Front of card */
  .card-front { left: 615px; top: 270px; }
  .dotted-frame {
    position: absolute; inset: 18px;
    border: 4px dotted var(--red);
  }
  .greeting {
    position: absolute; left: 0; right: 0; top: 92px; text-align: center;
    color: var(--red); font-weight: 600; font-size: 66px; letter-spacing: -0.5px;
    text-shadow: -2px 3px 0 var(--blue);
  }
  .accent-graphic {
    position: absolute; left: 120px; top: 184px; width: 200px; height: 20px;
    border-radius: 10px;
    background: linear-gradient(90deg, var(--red-soft), var(--red) 55%, var(--red-soft));
    opacity: 0.75;
  }
  .message {
    position: absolute; left: 0; right: 0; top: 228px; text-align: center;
    color: var(--ink); font-size: 17px; font-weight: 500; line-height: 1.5;
  }
  .front-brand {
    position: absolute; left: 50%; bottom: 8px; transform: translateX(-50%);
    background: var(--card); padding: 0 10px;
    display: flex; align-items: center; gap: 5px;
    color: var(--red); font-weight: 700; font-size: 14px; white-space: nowrap;
  }
  .front-brand .brand-mark { width: 7px; height: 7px; }
</style>
</head>
<body>
  <section class="card card-back">
    <div class="back-brand">
      <div class="brand-name"><span class="brand-mark"></span>Brightline<br>Electric Co.</div>
      <div class="dot-row"><span></span><span></span><span></span><span></span><span></span></div>
      <div class="contact">
        <div class="contact-line">
          <svg viewBox="0 0 10 10"><path d="M2 0 L4 2 L3 3.5 Q4.5 6 6.5 7 L8 6 L10 8 L8.5 10 Q3 9 0 1.5Z"/></svg>
          555-014-3254
          <svg viewBox="0 0 10 10"><rect x="2.5" y="0" width="5" height="10" rx="1"/></svg>
          555-016-3654
        </div>
        <div class="contact-line">
          <svg viewBox="0 0 10 10"><rect x="0" y="3" width="10" height="6" rx="1"/></svg>
          555-018-3541
          <svg viewBox="0 0 10 10"><rect x="0" y="2" width="10" height="7"/></svg>
          info@BrightlineElectric
        </div>
        <div>www.BrightlineElectric.com</div>
      </div>
    </div>
    <div class="divider"></div>
    <div class="stamp-box"></div>
    <div class="address-line"></div>
  </section>

  <section class="card card-front">
    <div class="dotted-frame"></div>
    <h1 class="greeting">Thank you</h1>
    <div class="accent-graphic" role="img" aria-label="Red lightning bolt swoosh graphic under the greeting"></div>
    <p class="message">for staying healthy &amp; safe during<br>the COVID-19 pandemic</p>
    <div class="front-brand"><span class="brand-mark"></span>Brightline Electric Co.</div>
  </section>
</body>
</html>
```